design a construction company business card

Design business card around our logo. Card must have all the typical info: name, title, address, phone, email, business name, etc. Somewhere on the card I would like to see our motto "Rooted in Honesty... Driven by Dedication." Consider adding a splash of bright orange to the card to complement the blues and silvers/grays in the logo. We are open to metallic inks, textures, etc. We would like to see options on both light and dark backgrounds. The font in the logo is Euro Technic Extended Regular.

```html
<!DOCTYPE html>
<html lang="en">
<head>
<meta charset="utf-8">
<title>Kestrel Builders, Inc. – Business Cards</title>
<link rel="stylesheet" href="https://fonts.googleapis.com/css2?family=Ubuntu:wght@400;500;700&display=swap">
<style>
  :root {
    --page-bg: #f1f1f1;
    --card-dark: #232323;
    --card-light: #ffffff;
    --brand-blue: #2268b5;
    --accent-orange: #f26a22;
    --text-dark: #2a2a2a;
    --text-light: #ffffff;
  }
  * { margin: 0; padding: 0; box-sizing: border-box; }
  html, body {
    width: 1200px; height: 1000px; overflow: hidden;
    background: var(--page-bg);
    font-family: "Ubuntu", sans-serif;
  }
  .card {
    position: absolute;
    width: 560px; height: 320px;
    overflow: hidden;
    box-shadow: 0 18px 40px rgba(0,0,0,.22);
  }
  /* Dark front */
  .card--front {
    left: 80px; top: 130px;
    background:
      repeating-linear-gradient(45deg, rgba(255,255,255,.025) 0 2px, transparent 2px 4px),
      var(--card-dark);
    display: flex; flex-direction: column; align-items: center; justify-content: center;
    gap: 14px;
  }
  .wordmark {
    display: flex; align-items: center; gap: 12px;
    color: var(--brand-blue);
    font-weight: 700; font-size: 34px; letter-spacing: 1px;
    white-space: nowrap;
  }
  .wordmark__mark { width: 22px; height: 22px; background: var(--brand-blue); }
  .motto {
    color: var(--accent-orange);
    font-size: 17px; letter-spacing: .3px;
  }
  /* Light back */
  .card--back { left: 560px; top: 540px; background: var(--card-light); }
  .card--back svg.swoosh { position: absolute; inset: 0; }
  .card--back .wordmark {
    position: absolute; left: 34px; top: 150px;
    font-size: 26px; gap: 10px;
  }
  .card--back .wordmark__mark { width: 18px; height: 18px; }
  .contact {
    position: absolute; left: 300px; top: 30px;
    color: var(--text-dark);
  }
  .contact__name { font-size: 21px; color: var(--brand-blue); font-weight: 400; }
  .contact__name strong { font-weight: 700; }
  .contact__title { font-size: 13px; margin-top: 2px; }
  .contact__title span { color: var(--brand-blue); }
  .contact__list { list-style: none; margin-top: 12px; }
  .contact__list li {
    display: flex; align-items: center; gap: 8px;
    font-size: 13.5px; height: 22px;
  }
  .icon { width: 17px; height: 17px; border-radius: 50%; flex: none; }
</style>
</head>
<body>

<section class="card card--front" aria-label="Business card front">
  <div class="wordmark"><span class="wordmark__mark"></span>Kestrel Builders, Inc.</div>
  <p class="motto">Rooted in Honesty... Driven by Dedication</p>
</section>

<section class="card card--back" aria-label="Business card back">
  <svg class="swoosh" width="560" height="320" viewBox="0 0 560 320" aria-hidden="true">
    <path d="M0,266 Q180,250 330,184 Q220,240 0,282 Z" fill="#f26a22"/>
    <path d="M0,294 Q300,276 560,150 L560,320 L0,320 Z" fill="#2268b5"/>
    <text x="250" y="300" transform="rotate(-17 250 300)" fill="#ffffff"
          font-family="Ubuntu, sans-serif" font-size="14" letter-spacing=".4">18/4 Harbour Rd, Eastvale NSW 2100</text>
  </svg>

  <div class="wordmark"><span class="wordmark__mark"></span>Kestrel Builders</div>

  <div class="contact">
    <h1 class="contact__name"><strong>DANA</strong> WHITFIELD</h1>
    <p class="contact__title">CEO of <span>Kestrel Builders, Inc</span></p>
    <ul class="contact__list">
      <li>
        <svg class="icon" viewBox="0 0 18 18" aria-hidden="true"><circle cx="9" cy="9" r="9" fill="#2268b5"/><path d="M6 5l2 0 1 2.5-1.2 1a6 6 0 0 0 2.7 2.7l1-1.2 2.5 1v2a1 1 0 0 1-1 1A8 8 0 0 1 5 6a1 1 0 0 1 1-1z" fill="#fff"/></svg>
        (02) 5550 1234</li>
      <li>
        <svg class="icon" viewBox="0 0 18 18" aria-hidden="true"><circle cx="9" cy="9" r="9" fill="#2268b5"/><rect x="6.2" y="4" width="5.6" height="10" rx="1" fill="none" stroke="#fff" stroke-width="1.3"/></svg>
        0400 555 012</li>
      <li>
        <svg class="icon" viewBox="0 0 18 18" aria-hidden="true"><circle cx="9" cy="9" r="9" fill="#2268b5"/><rect x="4.5" y="5.8" width="9" height="6.4" fill="#fff"/><path d="M4.5 5.8L9 9.4l4.5-3.6" fill="none" stroke="#2268b5" stroke-width="1"/></svg>
        info@kestrelbuilders.com</li>
      <li>
        <svg class="icon" viewBox="0 0 18 18" aria-hidden="true"><circle cx="9" cy="9" r="9" fill="#2268b5"/><circle cx="9" cy="9" r="4.8" fill="none" stroke="#fff" stroke-width="1.2"/><path d="M4.2 9h9.6M9 4.2v9.6" stroke="#fff" stroke-width="1"/></svg>
        www.kestrelbuilders.com</li>
    </ul>
  </div>
</section>

</body>
</html>
```